we are a mobile auto windscreen replacement business we are looking for a smart, stylish designed card on a matte black base color with large metallic silver KLT (similar to the vexapad box)
over the whole face of the card but down the bottom have (your local automotive & machinery glass specialist) & over the back

Reason: I'm looking for a design like no other something that really wows people to grab a card & use my business

Target Market(s)

Adults in western countries that own an automotive fleet company or anybody that owns a car

Industry/Entity Type

Automotive

Contact Information for Business Card

front: KLTautoglaze
Back: MORRIS 0438 62 57 84 Abn: 52807341196
morris@kltautoglaze.com.au & www.kltautoglaze.com.au

Logo styles of interest
Lettermark Logo
Requirements
Must have
• Metallic font on matte background
Nice to have
• 3D font that's glass or the word KLT smashed into glass on a black background I've added some pictures that maybe you could incorporate in the background or font it would be great to see a professionals ideas

```html
<!DOCTYPE html>
<html lang="en">
<head>
<meta charset="utf-8">
<title>KLT Business Card – Before and After</title>
<link rel="stylesheet" href="https://fonts.googleapis.com/css2?family=Arimo:wght@400;700&family=Crimson+Text:wght@400&display=swap">
<style>
  :root {
    --page: #ffffff;
    --ink: #000000;
    --card-black: #120d0c;
    --card-white: #ffffff;
    --card-border: #8a8a8a;
    --silver: #c9c9cc;
    --silver-dark: #4a4a4d;
    --tagline-red: #c0141c;
    --tagline-grey: #3c3c3c;
    --tagline-light: #d8d8d8;
    --contact-dark: #1a1a1a;
    --contact-light: #e6e6e6;
  }
  html, body {
    margin: 0;
    padding: 0;
    width: 1200px;
    height: 1000px;
    overflow: hidden;
    background: var(--page);
  }
  .sheet {
    position: relative;
    width: 1200px;
    height: 1000px;
    font-family: "Arimo", Arial, sans-serif;
  }
  .stage-label {
    position: absolute;
    left: 0;
    width: 1200px;
    text-align: center;
    font-size: 40px;
    color: var(--ink);
    margin: 0;
    line-height: 1;
  }
  .stage-label--before { top: 17px; }
  .stage-label--after { top: 440px; }

  .card {
    position: absolute;
    width: 578px;
    height: 333px;
    box-sizing: border-box;
    overflow: hidden;
  }
  .card--front { left: 23px; }
  .card--back { left: 611px; }
  .row-before { top: 60px; }
  .row-after { top: 487px; }

  .card__photo {
    position: absolute;
    inset: 0;
    background:
      radial-gradient(ellipse 60% 55% at 50% 45%, #6a6a70 0%, #2c2c30 45%, transparent 75%),
      linear-gradient(180deg, #1c1c20 0%, #3a3a40 55%, #0a0a0b 75%, #050505 100%);
  }
  .wordmark {
    position: absolute;
    font-family: "Arimo", Arial, sans-serif;
    font-weight: 700;
    color: var(--silver);
    letter-spacing: 2px;
    line-height: 1;
    margin: 0;
  }
  .card--front .wordmark {
    left: 0;
    width: 578px;
    text-align: center;
    top: 147px;
    font-size: 54px;
  }
  .card__tagline {
    position: absolute;
    font-variant: small-caps;
    letter-spacing: 1px;
    line-height: 17px;
    margin: 0;
  }
  .card--front .card__tagline {
    left: 0;
    width: 578px;
    text-align: center;
    top: 293px;
    font-size: 15px;
    color: var(--tagline-red);
  }

  .card--back.light {
    background: var(--card-white);
    border: 1px solid var(--card-border);
  }
  .card--back.dark {
    background: var(--card-black);
  }
  .card--back .wordmark {
    left: 52px;
    top: 80px;
    font-size: 68px;
  }
  .card--back.light .wordmark { color: var(--silver-dark); }
  .card--back .card__tagline {
    left: 311px;
    top: 110px;
    font-size: 15px;
    letter-spacing: 1.6px;
  }
  .card--back.light .card__tagline { color: var(--tagline-grey); }
  .card--back.dark .card__tagline { color: var(--tagline-light); }

  .contact {
    position: absolute;
    left: 311px;
    top: 222px;
    margin: 0;
    font-family: "Crimson Text", Georgia, serif;
    font-size: 16.5px;
    line-height: 21px;
  }
  .card--back.light .contact { color: var(--contact-dark); }
  .card--back.dark .contact { color: var(--contact-light); }
  .contact__name {
    font-size: 18px;
    letter-spacing: 0.5px;
    margin-right: 12px;
  }
  .contact p { margin: 0; }

  .comparison {
    position: absolute;
    left: 174px;
    top: 855px;
    width: 852px;
    height: 122px;
    background: var(--card-black);
  }
  .comparison .wordmark--small {
    left: 26px;
    top: 38px;
    font-size: 50px;
  }
  .comparison .wordmark--large {
    left: 522px;
    top: 23px;
    font-size: 80px;
  }
  .comparison__label {
    position: absolute;
    left: 254px;
    top: 22px;
    font-size: 29px;
    color: #ffffff;
    margin: 0;
    line-height: 1;
  }
  .comparison__arrow {
    position: absolute;
    left: 248px;
    top: 54px;
  }
</style>
</head>
<body>
<main class="sheet">
  <h2 class="stage-label stage-label--before">BEFORE</h2>

  <section class="card card--front row-before">
    <div class="card__photo" role="img" aria-label="Photograph of a dark sports car seen from the front with glowing headlights"></div>
    <p class="wordmark">KLT</p>
    <p class="card__tagline">Your Local Automotive &amp; Machinery Glass Specialist</p>
  </section>

  <section class="card card--back light row-before">
    <p class="wordmark">KLT</p>
    <p class="card__tagline">Your Local Automotive &amp;<br>Machinery Glass Specialist</p>
    <div class="contact">
      <p><span class="contact__name">MORRIS</span>0438 62 57 84</p>
      <p>Abn: 52807341196</p>
      <p>morris@kltautoglaze.com.au</p>
      <p>www.kltautoglaze.com.au</p>
    </div>
  </section>

  <h2 class="stage-label stage-label--after">AFTER</h2>

  <section class="card card--front row-after">
    <div class="card__photo" role="img" aria-label="Photograph of a dark sports car seen from the front with glowing headlights"></div>
    <p class="wordmark">KLT</p>
    <p class="card__tagline">Your Local Automotive &amp; Machinery Glass Specialist</p>
  </section>

  <section class="card card--back dark row-after">
    <p class="wordmark">KLT</p>
    <p class="card__tagline">Your Local Automotive &amp;<br>Machinery Glass Specialist</p>
    <div class="contact">
      <p><span class="contact__name">MORRIS</span>0438 62 57 84</p>
      <p>Abn: 52807341196</p>
      <p>morris@kltautoglaze.com.au</p>
      <p>www.kltautoglaze.com.au</p>
    </div>
  </section>

  <section class="comparison">
    <p class="wordmark wordmark--small">KLT</p>
    <p class="comparison__label">More Metallic</p>
    <svg class="comparison__arrow" width="236" height="16" viewBox="0 0 236 16" aria-hidden="true">
      <rect x="0" y="6" width="216" height="4" fill="#ffffff"/>
      <polygon points="214,0 236,8 214,16" fill="#ffffff"/>
    </svg>
    <p class="wordmark wordmark--large">KLT</p>
  </section>
</main>
</body>
</html>
```